Post card design for ( Interior ) & ( Exterior ) Residential Painting

We need a post card design for interior painting. To get homeowners to call about getting there interior home painted before the end winter comes, to get a clean, quality and no hassle paint job with low odor paints

Some IDEAS:
Exterior Paint Season is Coming to Northern VA and Metro DC!
Have you taken a look around your house this winter? Have you noticed any areas of unwanted moisture, mold or draft? Keeping your house painted and well-maintained on the outside will save money in the future as well. It protects your home from the elements – whether, wind, rain and snow or the strong summer sun.

idea #2
Exterior Paint Makes Your House Last Longer
aintaining a good coat of the correct type of paint on the exterior of your home will help protect your home from the elements and extend the overall life of the structure
idea #3
Rotten Wood and Two Other TOP Reasons for Exterior Paint
We’ll start there – rotten wood – the first reason for exterior paint. If your home or building has decorative wood trim, wood siding or even wood around windows and doors, it could be at risk for rotten or rotting wood. Maintaining a healthy and COMPLETE coat of paint will protect the wood from water damage. Additionally, during a paint project, our team can assess wooden areas and advise if there are any places of concern. For a long-term solution, consider replacing wood trim with vinyl or wood alternatives that stand up to the elements. This can also be done during an exterior paint project.
Idea # 4
Benefits of Using Low-VOC interior Paints
Paints with low-VOC or Zero-VOC are considered healthier options due to the lower amount of toxins they release when applied to a wall. Latex paints are popular low-VOC because they are water based and don’t contain other chemicals you may find in oil-based paints.

Less odor! Because these paints have lower levels of toxins that are released, the paint smell that is associated with a fresh coat of paint is not as strong. Low-VOC would be a great option if you plan on painting a nursery because the smell won’t linger. Although you might not smell it, it is always important to ventilate the room. All paints, even low-VOC have levels of toxicity which are not good to breathe in for long periods of time.

Target Market(s)

single family homes

Colors

Designer to choose colors to be used in the design.

Requirements
Should not have
• cheep, free

```html
<!DOCTYPE html>
<html lang="en">
<head>
<meta charset="utf-8">
<title>Brightline Painting – Postcard</title>
<link rel="stylesheet" href="https://fonts.googleapis.com/css2?family=Montserrat:wght@500;600;700;800&family=Lato:ital,wght@1,400;1,700&display=swap">
<style>
  :root{
    --red:#e21d3f;
    --ink:#1d1d1f;
    --charcoal:#2a2a2c;
    --white:#ffffff;
    --rule:#8a8a8a;
    --stage:#e6e6e6;
  }
  *{box-sizing:border-box;margin:0;padding:0}
  html,body{width:902px;height:1200px;overflow:hidden}
  body{background:var(--stage);font-family:"Montserrat",sans-serif;color:var(--ink);position:relative}
  .card{position:absolute;width:670px;height:455px;background:var(--white);overflow:hidden;box-shadow:0 6px 14px rgba(0,0,0,.25)}
  .card svg.shapes{position:absolute;inset:0}
  .abs{position:absolute}

  .brand{font-weight:800;color:var(--ink);line-height:1;letter-spacing:-.3px;display:flex;align-items:flex-start}
  .brand-mark{flex:none;background:var(--red)}

  /* front */
  .front{left:73px;top:85px}
  .front .brand{left:26px;top:50px;font-size:26px;gap:8px}
  .front .brand-mark{width:12px;height:12px;margin-top:7px}
  .front .headline{left:292px;top:36px;width:372px;text-align:center;color:var(--white);font-weight:700;font-size:23px;white-space:nowrap;line-height:1.1}
  .front .subline{left:292px;top:66px;width:372px;text-align:center;color:var(--white);font-weight:700;font-size:13px;white-space:nowrap}
  .photo{position:absolute;border:2px solid var(--ink)}
  .photo.one{left:268px;top:100px;width:172px;height:128px;background:linear-gradient(90deg,#d9dbe0 0%,#b9bcc4 48%,#8d98a8 52%,#c4c9d1 100%)}
  .photo.two{left:449px;top:100px;width:192px;height:128px;background:linear-gradient(90deg,#8a4a38 0%,#a6624c 45%,#3e5fa8 55%,#d5d3cc 100%)}
  .home-photo{left:30px;top:163px;width:156px;height:156px;border-radius:50%;border:4px solid var(--white);background:radial-gradient(circle at 50% 40%,#d9c9a6 0%,#8d8c8c 45%,#3d6a3a 90%)}
  .front .questions{left:200px;top:248px;width:455px;text-align:right;color:var(--white);font-weight:600;font-size:14.5px;line-height:1.35}
  .front .body{left:190px;top:328px;width:472px;height:86px;font-weight:600;font-size:12px;line-height:1.36;color:var(--ink)}
  .front .body .stripe-gap{float:left;width:110px;height:86px;shape-outside:polygon(0 0,66px 0,108px 86px,0 86px)}
  .front .body em{font-style:normal;color:var(--red)}
  .contact-label{left:0;top:346px;width:236px;text-align:center;color:var(--white);font-weight:600;font-size:13px}
  .front .phone{left:0;top:370px;width:236px;display:flex;justify-content:center;align-items:center;gap:5px;color:var(--white);font-weight:700;font-size:22px}
  .front .cta{left:0;top:408px;width:236px;text-align:center;color:var(--white);font-weight:600;font-size:13px;line-height:1.3}
  .front .visit{left:288px;top:425px;width:370px;display:flex;align-items:center;gap:10px;color:var(--white);font-weight:600;font-size:14px}
  .front .visit .label{color:var(--ink);margin-right:4px}
  .icon{display:inline-block;flex:none}

  /* back */
  .back{left:176px;top:665px}
  .back .title{left:36px;top:32px;color:var(--white);font-weight:700;font-size:18px;line-height:1.35;white-space:nowrap}
  .back .subhead{left:32px;top:97px;color:var(--white);font-weight:600;font-size:14px;line-height:1.3;white-space:nowrap}
  .checklist{left:32px;top:158px;width:335px;list-style:none;font-family:"Lato",sans-serif;font-style:italic;font-size:11px;line-height:1.35;color:var(--ink)}
  .checklist li{display:flex;gap:10px;margin-bottom:8px}
  .back .contact{left:40px;top:378px;display:flex;align-items:center;gap:8px;color:var(--red);font-weight:600;font-size:13px}
  .back .contact .num{color:var(--white);font-weight:700;font-size:23px}
  .back .visit{left:38px;top:414px;display:flex;align-items:center;gap:8px;color:var(--red);font-weight:600;font-size:13px}
  .back .visit .url{color:var(--white)}
  .back .brand{left:442px;top:42px;font-size:16px;gap:6px}
  .back .brand-mark{width:8px;height:8px;margin-top:4px}
  .stamp{left:590px;top:34px;width:68px;height:60px;border:1px solid var(--rule)}
  .address-line{left:430px;width:232px;height:1px;background:var(--rule)}
</style>
</head>
<body>

<section class="card front" aria-label="Postcard front">
  <svg class="shapes" width="670" height="455" viewBox="0 0 670 455" aria-hidden="true">
    <polygon points="296,0 670,0 670,236 196,236" fill="var(--red)"/>
    <polygon points="284,0 290,0 190,236 184,236" fill="var(--red)"/>
    <polygon points="272,0 278,0 178,236 172,236" fill="var(--red)"/>
    <polygon points="260,0 266,0 166,236 160,236" fill="var(--red)"/>
    <rect x="190" y="236" width="480" height="68" fill="var(--charcoal)"/>
    <rect x="0" y="310" width="250" height="145" fill="var(--charcoal)"/>
    <rect x="0" y="360" width="236" height="36" fill="var(--red)"/>
    <polygon points="190,304 260,304 330,455 250,455" fill="var(--white)"/>
    <polygon points="204,304 212,304 282,455 274,455" fill="var(--red)"/>
    <polygon points="218,304 226,304 296,455 288,455" fill="var(--red)"/>
    <polygon points="232,304 240,304 310,455 302,455" fill="var(--red)"/>
    <polygon points="262,414 670,414 670,455 281,455" fill="var(--red)"/>
  </svg>

  <div class="abs brand"><span class="brand-mark"></span><span>Brightline<br>Painting</span></div>
  <div class="abs home-photo" role="img" aria-label="Photo of a two-storey family home at dusk with lit windows and a green lawn"></div>

  <h1 class="abs headline">EXTERIOR PAINT SEASON</h1>
  <p class="abs subline">IS COMINGTO NORTHERN VA AND METRO DC!</p>
  <div class="photo one" role="img" aria-label="Before and after photo of a repainted white siding wall"></div>
  <div class="photo two" role="img" aria-label="Before and after photo of a brick house with freshly painted blue shutters"></div>

  <p class="abs questions">Have you taken a look around your house this winter?<br>Have you noticed any areas of unwanted moisture,<br>mold or draft?</p>
  <div class="abs body"><span class="stripe-gap"></span>Keeping your house painted and well-maintained on the outside will save money in the future as well. It protects your home from the elements – <em>whether, wind, rain and snow or the strong summer sun.</em></div>

  <p class="abs contact-label">CONTACT US</p>
  <p class="abs phone">
    <svg class="icon" width="20" height="20" viewBox="0 0 20 20" aria-hidden="true"><circle cx="10" cy="10" r="8.5" fill="none" stroke="#fff" stroke-width="1.6"/><path d="M7 5.5l1.6 2.4-1 1.1c.6 1.3 1.5 2.2 2.7 2.8l1.1-1 2.4 1.6-.9 1.8c-3.4-.3-6.4-3.3-6.7-6.8z" fill="#fff"/></svg>
    555-014-2271
  </p>
  <p class="abs cta">BOOK ESTIMATE<br>APPOINTMENT NOW</p>
  <p class="abs visit"><span class="label">Visit us today :</span>
    <svg class="icon" width="13" height="13" viewBox="0 0 14 14" aria-hidden="true"><g fill="none" stroke="#fff" stroke-width="1.2"><circle cx="7" cy="7" r="6"/><ellipse cx="7" cy="7" rx="2.6" ry="6"/><path d="M1 7h12"/></g></svg>
    www.brightlinepainting.com</p>
</section>

<section class="card back" aria-label="Postcard back">
  <svg class="shapes" width="670" height="455" viewBox="0 0 670 455" aria-hidden="true">
    <polygon points="0,0 418,0 408,92 0,92" fill="var(--red)"/>
    <rect x="0" y="92" width="370" height="52" fill="var(--charcoal)"/>
    <rect x="0" y="370" width="370" height="85" fill="var(--charcoal)"/>
    <polygon points="418,0 426,0 384,455 376,455" fill="var(--red)"/>
    <polygon points="430,0 436,0 394,455 388,455" fill="var(--red)"/>
    <polygon points="440,0 446,0 404,455 398,455" fill="var(--red)"/>
  </svg>

  <h2 class="abs title">ROTTEN WOOD AND TWO OTHER TOP<br>REASONS FOR EXTERIOR PAINT</h2>
  <p class="abs subhead">WE’LL START THERE – ROTTEN WOOD<br>– THE FIRST REASON FOR EXTERIOR PAINT.</p>

  <ul class="abs checklist">
    <li><svg class="icon" width="13" height="13" viewBox="0 0 13 13" aria-hidden="true"><rect x="1" y="2" width="10" height="10" fill="none" stroke="var(--red)" stroke-width="1.2"/><path d="M3 7l2.5 2.5L12 1.5" fill="none" stroke="var(--red)" stroke-width="1.8"/></svg><span>If your home or building has decorative wood trim, wood siding or even wood around windows and doors, it could be at risk for rotten or rotting wood.</span></li>
    <li><svg class="icon" width="13" height="13" viewBox="0 0 13 13" aria-hidden="true"><rect x="1" y="2" width="10" height="10" fill="none" stroke="var(--red)" stroke-width="1.2"/><path d="M3 7l2.5 2.5L12 1.5" fill="none" stroke="var(--red)" stroke-width="1.8"/></svg><span>Maintaining a healthy and COMPLETE coat of paint will protect the wood from water damage.</span></li>
    <li><svg class="icon" width="13" height="13" viewBox="0 0 13 13" aria-hidden="true"><rect x="1" y="2" width="10" height="10" fill="none" stroke="var(--red)" stroke-width="1.2"/><path d="M3 7l2.5 2.5L12 1.5" fill="none" stroke="var(--red)" stroke-width="1.8"/></svg><span>Additionally, during a paint project, our team can assess wooden areas and advise if there are any places of concern.</span></li>
    <li><svg class="icon" width="13" height="13" viewBox="0 0 13 13" aria-hidden="true"><rect x="1" y="2" width="10" height="10" fill="none" stroke="var(--red)" stroke-width="1.2"/><path d="M3 7l2.5 2.5L12 1.5" fill="none" stroke="var(--red)" stroke-width="1.8"/></svg><span>For a long-term solution, consider replacing wood trim with vinyl or wood alternatives that stand up to the elements.</span></li>
    <li><svg class="icon" width="13" height="13" viewBox="0 0 13 13" aria-hidden="true"><rect x="1" y="2" width="10" height="10" fill="none" stroke="var(--red)" stroke-width="1.2"/><path d="M3 7l2.5 2.5L12 1.5" fill="none" stroke="var(--red)" stroke-width="1.8"/></svg><span>This can also be done during an exterior paint project.</span></li>
  </ul>

  <p class="abs contact">CONTACT US :
    <svg class="icon" width="22" height="22" viewBox="0 0 20 20" aria-hidden="true"><circle cx="10" cy="10" r="8.5" fill="none" stroke="#fff" stroke-width="1.6"/><path d="M7 5.5l1.6 2.4-1 1.1c.6 1.3 1.5 2.2 2.7 2.8l1.1-1 2.4 1.6-.9 1.8c-3.4-.3-6.4-3.3-6.7-6.8z" fill="#fff"/></svg>
    <span class="num">555-014-2271</span></p>
  <p class="abs visit">Visit us today :
    <svg class="icon" width="12" height="12" viewBox="0 0 14 14" aria-hidden="true"><g fill="none" stroke="#fff" stroke-width="1.2"><circle cx="7" cy="7" r="6"/><ellipse cx="7" cy="7" rx="2.6" ry="6"/><path d="M1 7h12"/></g></svg>
    <span class="url">www.brightlinepainting.com</span></p>

  <div class="abs brand"><span class="brand-mark"></span><span>Brightline<br>Painting</span></div>
  <div class="abs stamp" aria-hidden="true"></div>
  <div class="abs address-line" style="top:228px"></div>
  <div class="abs address-line" style="top:276px"></div>
  <div class="abs address-line" style="top:326px"></div>
</section>

</body>
</html>
```